Civic Counsel and Advocacy Alliance Event

Situation:
- Civic Counsel and Advocacy Alliance will host a fundraising event at Cellar of Amber Oak to create fundraising momentum for the year
- Event tickets will be $200
- The event will be a social/networking event for professional in the Detroit area
- DJ Lowell Varnick, a well know Detroit area DJ will DJ the event
- Hon. Marla Penwright-Osei, M.Ed. will be the featured speaker/host of the event
- CCA CEO will also be a speaker
- Proceeds from the event will go toward expungement, which is a hot top in Michigan, as s new expungement reform law has been enacted in the state

Objectives:
- Raise fund through ticket sales to support expungement and general CCA programs/services
- Gain event sponsors

Messaging:
- Highlight details about the event and the wine tasting/networking experience
- Inspire people to attend the event in support of a worthy cause
- Event Details:
- Event Name: The Vintage & Supper Soirée
o Date: Thursday, September 30, 2021
o Time: 5:30 PM – 8:30 PM
o Space limited, get your ticket today to ensure access to this exclusive event
o Sample various high-quality wines and custom pairings, while helping Civic Counsel and Advocacy Alliance make a difference in our community.
o Proceeds from the event will support Expungement, Domestic Violence prevention, an various CCA programs helping those in need of legal representation.

Target Market(s)

- Attorneys/Professionals in Southeast Michigan - Affluent donors/philanthropist

Industry/Entity Type

Legal/Networking Event

Colors
0054AA
0677BA
7BADD7
CADEEF
E8F1F8
FFF300
FFF600
FEFA6F
FFFEC7
FFFEE8

Requirements
Nice to have
• Must be fun and inviting

```html
<!DOCTYPE html>
<html lang="en">
<head>
<meta charset="utf-8">
<title>The Vintage &amp; Supper Soirée — Event Flyer</title>
<link rel="stylesheet" href="https://fonts.googleapis.com/css2?family=Bebas+Neue&family=Archivo+Black&family=Oswald:wght@300&family=Roboto+Condensed:wght@700&family=Montserrat:wght@400;600;700&display=swap">
<style>
  :root {
    --page-bg: #d6d6d6;
    --paper: #ffffff;
    --navy: #2c4a8e;
    --royal: #0677ba;
    --sky: #7badd7;
    --yellow: #fff300;
    --ink: #333333;
    --body-ink: #4a4a4a;
    --brand-ink: #2c3e6e;
  }
  * { box-sizing: border-box; margin: 0; padding: 0; }
  html, body {
    width: 1200px; height: 2282px; overflow: hidden;
    background: var(--page-bg);
  }
  .flyer {
    position: absolute; left: 40px; top: 356px;
    width: 777px; height: 1089px;
    background: var(--paper);
    transform: scale(1.4414); transform-origin: 0 0;
    box-shadow: 0 6px 18px rgba(0,0,0,.25);
    overflow: hidden;
  }
  .corner-tab { position: absolute; left: 0; top: 0; width: 80px; height: 108px; background: var(--sky); }
  .brand {
    position: absolute; left: 92px; top: 30px; display: flex; align-items: center; gap: 12px;
  }
  .brand-mark { width: 54px; height: 54px; border-radius: 50%; background: var(--brand-ink); }
  .brand-name {
    font-family: "Montserrat", sans-serif; font-weight: 600; font-size: 12.5px;
    line-height: 1.25; color: var(--brand-ink); letter-spacing: .4px; width: 210px;
  }
  .title-panel {
    position: absolute; left: 0; top: 108px; width: 403px; height: 317px; background: var(--navy);
    padding: 54px 0 0 43px;
  }
  .title {
    font-family: "Bebas Neue", sans-serif; font-weight: 400; font-size: 78px;
    line-height: 78px; color: #fff; white-space: nowrap;
  }
  .title .accent { color: var(--yellow); }
  .date-tag {
    position: absolute; left: 46px; top: 460px; width: 88px; height: 198px; background: var(--yellow);
    display: flex; align-items: center; justify-content: center;
  }
  .date-tag span {
    transform: rotate(-90deg); font-family: "Roboto Condensed", sans-serif; font-weight: 700;
    font-size: 74px; color: var(--navy); letter-spacing: -2px; line-height: 1;
  }
  .date-day {
    position: absolute; left: 145px; top: 458px;
    font-family: "Archivo Black", sans-serif; font-size: 36px; line-height: 40px; color: var(--ink);
  }
  .date-month {
    position: absolute; left: 145px; top: 496px; white-space: nowrap;
    font-family: "Bebas Neue", sans-serif; font-size: 52px; line-height: 48px; color: var(--navy);
  }
  .date-year {
    position: absolute; left: 143px; top: 540px; white-space: nowrap;
    font-family: "Bebas Neue", sans-serif; font-size: 152px; line-height: 124px; color: var(--ink);
    letter-spacing: 2px;
  }
  .time-line {
    position: absolute; left: 46px; top: 686px; white-space: nowrap;
    font-size: 44px; line-height: 44px; color: var(--navy);
  }
  .time-line .label { font-family: "Oswald", sans-serif; font-weight: 300; font-size: 36px; letter-spacing: -1px; }
  .time-line .hours { font-family: "Bebas Neue", sans-serif; color: var(--ink); }
  .details { position: absolute; left: 46px; top: 748px; width: 330px; }
  .details p {
    font-family: "Montserrat", sans-serif; font-size: 13.2px; line-height: 17px; color: var(--body-ink);
  }
  .details .divider { border: 0; border-top: 2px dotted #9a9a9a; margin: 20px 0 19px; width: 330px; }
  .web-bar {
    position: absolute; left: 0; top: 1005px; width: 308px; height: 37px; background: var(--royal);
    border-radius: 0 7px 7px 0; padding-left: 46px;
    font-family: "Montserrat", sans-serif; font-weight: 700; font-size: 19px; line-height: 37px; color: #fff;
  }
  .photo { position: absolute; left: 418px; width: 359px; }
  .photo-bottles { top: 0; height: 358px; background: linear-gradient(100deg, #1b1410 0%, #4a3324 45%, #7d5a3a 100%); }
  .photo-guests { top: 372px; height: 333px; background: linear-gradient(160deg, #26357a 0%, #1c2658 100%); }
  .photo-tasting { top: 720px; height: 369px; background: linear-gradient(140deg, #2b2a2c 0%, #4a413d 55%, #8a6c58 100%); }
</style>
</head>
<body>
  <main class="flyer">
    <div class="corner-tab"></div>
    <div class="brand">
      <div class="brand-mark"></div>
      <div class="brand-name">CIVIC COUNSEL AND ADVOCACY ALLIANCE</div>
    </div>

    <section class="title-panel">
      <h1 class="title">The Vintage &amp;<br>Supper<br><span class="accent">Soirée</span></h1>
    </section>

    <div class="date-tag"><span>DATE</span></div>
    <div class="date-day">THURSDAY</div>
    <div class="date-month">SEPTEMBER 30</div>
    <div class="date-year">2021</div>

    <div class="time-line"><span class="label">TIME:</span> <span class="hours">5:30 PM — 8:30 PM</span></div>

    <div class="details">
      <p>Space limited, get your ticket today to ensure access to this exclusive event</p>
      <hr class="divider">
      <p>Sample various high-quality wines and custom pairings, while helping Civic Counsel and Advocacy Alliance make a difference in our community.</p>
      <hr class="divider">
      <p>Proceeds from the event will support Expungement, Domestic Violence prevention, an various CCA programs helping those in need of legal representation.</p>
    </div>

    <div class="web-bar">www.ccaadetroit.org</div>

    <div class="photo photo-bottles" role="img" aria-label="Close-up photo of dark wine bottles lined up on a counter"></div>
    <div class="photo photo-guests" role="img" aria-label="Navy-tinted photo of guests mingling at a wine tasting"></div>
    <div class="photo photo-tasting" role="img" aria-label="Photo of a guest reaching for a charcuterie board with wine glasses on a table"></div>
  </main>
</body>
</html>
```